Brand New Product Needs Sales Focused Website Design

Looking for design of Homepage, Category Page & Product Page for single product sales focused website. TrendaCrate manufacture and distribute a brand new product to the market called FoldiPal-Crate which is a super strong, re-useable, folding & stacking plastic box which can be seen on our current website www.foldipal-crate.example FoldiPal-Crate was originally developed as an alternative to supermarket carrier bags and was pitched as a box for life against the other low end re-useable products. The original version was made from recycled plastic and pitched very much as environmental product. We are now taking a different direction and have re-designed the boxes in 5 bright and fashionable designs and although we still want the primary focus to be supermarket shopping we want to position the product as a design led, must have shopping and household accessory rather than a boring, cheap looking black plastic box. The new designs will still have the environmental benefits of being able to be re-used thousands of times and being 100% recyclable and save on the imminent 5p tax on carrier bags in the UK however the new designs will not be made from recycled material. Although the main use for FoldiPal-Crate is supermarket shopping it has a multitude of other uses especially where you need temporary storage - laundry, back of the car, moving house/students, gardening, days out, home office filing (will take A4 file), recycling and much more - FoldiPal-Crate is made out of super strong Polypropylene and can be easily washed and sanitised after use and can be folded and unfolded thousands of times and so will last for many years. FoldiPal-Crate is a product that needs to be seen in action to be understood so the web design must quickly and easily communicate what FoldiPal-Crate is and how it works - this can be done with video, images and copy. Our current website does not work for many reasons:- it is too busy, has too much information, tries too hard and ultimately isn't working. Any of the images off our current website can be supplied for use. Once the concept of the website is agreed I can get these photoshopped with the new designs. Pictures of new designs for reference will be attached to this brief. Ultimately we want the website to convert visitors to sales and therefore designers with a proven track record in this field are especially welcome to enter. We also have a Fileharbor folder with over 100 product and situation images in - please send email address and we will send an invite to the folder. Due to Christmas period this competition will be run over 15 days however we may choose to extend the deadline to account for the non working days. Any questions feel free to ask - we will respond within 24 hours where possible.

```html
<!DOCTYPE html>
<html lang="en">
<head>
<meta charset="utf-8">
<title>FoldiPal - Crate | My Black FoldiPal Crate</title>
<link href="https://fonts.googleapis.com/css2?family=Caladea&family=Arimo:wght@400;700&display=swap" rel="stylesheet">
<style>
:root{
  --teal:#21ad8f;
  --teal-text:#1fa88a;
  --mint:#aeeee2;
  --panel-top:#9ee6d6;
  --panel-bottom:#c1f2ea;
  --ink:#111;
  --white:#fff;
  --footer:#2d2d2d;
  --olive:#6b6b12;
  --orange:#f5a000;
  --rust:#b85d00;
  --star:#f59a00;
  --tick:#2fb52f;
  --cart:#6e3a12;
}
*{box-sizing:border-box;margin:0;padding:0}
html,body{width:1200px;height:1129px;overflow:hidden}
body{position:relative;background:var(--mint);font-family:"Arimo",Arial,sans-serif;color:var(--ink)}
.abs{position:absolute}
.top-stripe{left:0;top:0;width:1200px;height:5px;
  background:repeating-linear-gradient(90deg,var(--olive) 0 73px,var(--orange) 73px 146px,var(--olive) 146px 219px,var(--rust) 219px 292px)}
.site-header{left:0;top:5px;width:1200px;height:115px;background:var(--white);border-bottom:5px solid var(--teal)}
.brand{left:81px;top:22px;font-family:"Caladea",Georgia,serif;font-size:54px;color:#000;line-height:1}
.tagline{left:536px;top:35px;font-family:"Caladea",Georgia,serif;font-size:42px;color:var(--teal-text);line-height:1}
.header-cart{left:1126px;top:37px}
.product-title{left:476px;top:141px;width:248px;height:53px;background:var(--white);border:2px solid var(--teal);
  font-family:"Caladea",Georgia,serif;font-size:23px;display:flex;align-items:center;justify-content:center}
.main-photo{left:102px;top:213px;width:351px;height:272px;border:2px solid var(--teal);
  background:linear-gradient(135deg,#f4f4f4 0%,#1a1a1a 45%,#111 60%,#1eb06c 100%)}
.thumb{top:494px;width:99px;height:73px;border:1px solid var(--teal);background:linear-gradient(135deg,#f0f0f0,#151515 55%,#1eb06c)}
.price{left:478px;top:214px;font-size:21px}
.add-basket{left:477px;top:249px;width:159px;height:30px;background:var(--white);border:1px solid var(--teal);
  font-family:"Caladea",Georgia,serif;font-size:18px;color:var(--teal-text);display:flex;align-items:center;justify-content:center;gap:6px}
.details{left:478px;top:304px;width:636px;height:414px;border:1px solid var(--teal);
  background:linear-gradient(170deg,var(--panel-top),var(--panel-bottom));padding:17px 12px 0 11px;font-size:13.5px;line-height:23px}
.details p{margin-bottom:23px}
.details p+p{margin-bottom:6px}
.features{list-style:none}
.features li{position:relative;padding-left:28px;line-height:31px}
.features li.wrap{line-height:31px}
.features svg{position:absolute;left:1px;top:9px}
.reviews{left:0;top:768px;width:1200px;height:226px;background:var(--teal);color:var(--white)}
.reviews h2{position:absolute;left:0;width:1200px;top:12px;text-align:center;font-family:"Caladea",Georgia,serif;font-weight:400;font-size:22px}
.review-photo{left:76px;top:52px;width:249px;height:156px;border:4px solid var(--white);border-radius:6px;
  background:linear-gradient(120deg,#8b1c1c 0%,#d9d6cf 35%,#5a5a5a 60%,#2446c8 85%,#1a1a1a)}
.quote{left:350px;top:52px;width:580px;font-size:15.5px;line-height:23px}
.reviewer{left:350px;top:120px;font-size:15.5px}
.stars{left:347px;top:146px}
.write-review{left:347px;top:176px;width:193px;height:31px;background:var(--white);color:var(--teal-text);
  font-weight:700;font-size:15.5px;display:flex;align-items:center;justify-content:center}
.share{left:556px;top:182px;font-size:16.5px}
.site-footer{left:0;top:994px;width:1200px;height:135px;background:var(--footer);color:var(--white)}
.footer-nav a{position:absolute;top:22px;color:var(--white);text-decoration:none;font-family:"Caladea",Georgia,serif;font-size:17px}
.copyright{left:79px;top:68px;font-size:13px}
.copyright span{color:var(--teal-text);font-weight:700}
.social{top:54px;width:48px;height:48px;border-radius:50%;border:2px solid var(--white)}
.social.first{background:var(--white);border-color:var(--teal)}
</style>
</head>
<body>
<div class="abs top-stripe"></div>
<header class="abs site-header">
  <div class="abs brand">FoldiPal - Crate</div>
  <div class="abs tagline">Designed For Life. Made To Last.</div>
  <svg class="abs header-cart" width="54" height="54" viewBox="0 0 54 54" aria-label="Basket">
    <path d="M2 6h9l7 30h28l6-22H14" fill="none" stroke="var(--cart)" stroke-width="4" stroke-linejoin="round"/>
    <path d="M16 20h34M18 28h30M24 14v22M32 14v22M40 14v22" stroke="var(--cart)" stroke-width="2"/>
    <circle cx="21" cy="45" r="4" fill="var(--cart)"/><circle cx="42" cy="45" r="4" fill="var(--cart)"/>
  </svg>
</header>

<main>
  <h1 class="abs product-title" style="font-weight:400">My Black FoldiPal Crate</h1>
  <div class="abs main-photo" role="img" aria-label="Person carrying an open black folding crate"></div>
  <div class="abs thumb" style="left:104px" role="img" aria-label="Crate held open"></div>
  <div class="abs thumb" style="left:224px;background:#111" role="img" aria-label="Crate folded flat as a briefcase"></div>
  <div class="abs thumb" style="left:344px" role="img" aria-label="Crate carried by its handles"></div>

  <div class="abs price">£14.99</div>
  <div class="abs add-basket">Add to Basket
    <svg width="22" height="19" viewBox="0 0 22 19"><path d="M0 1h4l3 11h11l3-8H5" fill="var(--teal)" stroke="var(--teal)" stroke-width="2"/><circle cx="8" cy="16" r="2" fill="var(--teal)"/><circle cx="17" cy="16" r="2" fill="var(--teal)"/></svg>
  </div>

  <section class="abs details">
    <p>The Consumer has already been educated into the ‘Bag For Life’ concept of shopping –<br>FoldiPal-Crate is the perfect answer to those regular customers visiting the store by car and<br>particularly appeals to the ‘heavy’ shopper .</p>
    <p>A rigid stackable box when open, it folds flat into a convenient, compact lightweight ‘briefcase’ for<br>carrying or storage. Using the principles of origami, it folds down and is held together by<br>self-fastenings.</p>
    <ul class="features">
      <li><svg width="19" height="16" viewBox="0 0 19 16"><path d="M1 9l6 6L18 2" fill="none" stroke="var(--tick)" stroke-width="4"/></svg>Folded ‘briefcase’ size: 32 x 25 x 4cm.</li>
      <li><svg width="19" height="16" viewBox="0 0 19 16"><path d="M1 9l6 6L18 2" fill="none" stroke="var(--tick)" stroke-width="4"/></svg>Open 32 x 25 x 55cm.</li>
      <li><svg width="19" height="16" viewBox="0 0 19 16"><path d="M1 9l6 6L18 2" fill="none" stroke="var(--tick)" stroke-width="4"/></svg>Opens out in seconds into a lightweight, strong, rigid, stackable box</li>
      <li><svg width="19" height="16" viewBox="0 0 19 16"><path d="M1 9l6 6L18 2" fill="none" stroke="var(--tick)" stroke-width="4"/></svg>Ergonomically designed with comfy handholds</li>
      <li class="wrap"><svg width="19" height="16" viewBox="0 0 19 16"><path d="M1 9l6 6L18 2" fill="none" stroke="var(--tick)" stroke-width="4"/></svg>Tested to be able to carry in excess of 20kg – more than the average<br>customer can lift and carry.</li>
      <li><svg width="19" height="16" viewBox="0 0 19 16"><path d="M1 9l6 6L18 2" fill="none" stroke="var(--tick)" stroke-width="4"/></svg>Fits into most Supermarket trolleys</li>
    </ul>
  </section>
</main>

<section class="abs reviews">
  <h2>Customer Reviews</h2>
  <div class="abs review-photo" role="img" aria-label="Shopper packing groceries into a crate at a supermarket checkout"></div>
  <p class="abs quote">An easy 5 Star from me – so easy to use at the checkout for my weekly shop – no<br>more bags for me!</p>
  <p class="abs reviewer">Bella Marsh From Doncaster</p>
  <svg class="abs stars" width="120" height="22" viewBox="0 0 120 22" aria-label="4 stars">
    <g fill="var(--star)">
      <polygon points="11,1 13.6,8 21,8 15,12.6 17.3,20 11,15.5 4.7,20 7,12.6 1,8 8.4,8"/>
      <polygon transform="translate(31 0)" points="11,1 13.6,8 21,8 15,12.6 17.3,20 11,15.5 4.7,20 7,12.6 1,8 8.4,8"/>
      <polygon transform="translate(62 0)" points="11,1 13.6,8 21,8 15,12.6 17.3,20 11,15.5 4.7,20 7,12.6 1,8 8.4,8"/>
      <polygon transform="translate(93 0)" points="11,1 13.6,8 21,8 15,12.6 17.3,20 11,15.5 4.7,20 7,12.6 1,8 8.4,8"/>
    </g>
  </svg>
  <div class="abs write-review">Write &nbsp;an online review</div>
  <p class="abs share">and share your thoughts with other shoppers!</p>
</section>

<footer class="abs site-footer">
  <nav class="footer-nav">
    <a href="#" style="left:389px">Home</a>
    <a href="#" style="left:500px">Terms &amp; Condition</a>
    <a href="#" style="left:730px">Contact Us</a>
  </nav>
  <p class="abs copyright">© <span>FoldiPal-Crate</span> - 2014. All Rights Reserved.</p>
  <div class="abs social first" style="left:874px"></div>
  <div class="abs social" style="left:956px"></div>
  <div class="abs social" style="left:1039px"></div>
</footer>
</body>
</html>
```